amber crest health and wellness group.

need a full website design , all information provided in word document labeled website blue print

Target Market(s)

first responders, military , people in crisis

Coding

Coded - Design and coding required

Number of Pages Required

1 page

```html
<!DOCTYPE html>
<html lang="en">
<head>
<meta charset="utf-8">
<title>Amber Crest Health &amp; Wellness Group</title>
<link rel="stylesheet" href="https://fonts.googleapis.com/css2?family=Montserrat:wght@500;600;700;800;900&family=Inter:wght@300;400;500&display=swap">
<style>
:root{
  --navy:#1f4580;
  --navy-dark:#173766;
  --ink:#1d1d1f;
  --black:#000;
  --white:#fff;
  --mist:#f1f1f3;
  --line:#b9c3d4;
  --body:#2b2b2b;
}
*{box-sizing:border-box;margin:0;padding:0}
html,body{width:1200px;height:4147px;overflow:hidden}
body{position:relative;background:var(--white);font-family:"Inter",sans-serif;color:var(--body)}
.abs{position:absolute}
.heading{font-family:"Montserrat",sans-serif;font-weight:800;color:var(--navy);text-transform:uppercase;letter-spacing:.5px}
.rule{position:absolute;height:2px;width:48px;background:var(--navy)}
.btn{position:absolute;display:flex;align-items:center;justify-content:center;background:var(--navy);color:var(--white);font-family:"Montserrat",sans-serif;font-weight:700;text-transform:uppercase}
.photo{position:absolute}

/* header */
.site-header{position:absolute;left:0;top:0;width:1200px;height:121px;background:var(--black)}
.brand{position:absolute;left:153px;top:30px;width:130px;color:var(--navy);font-family:"Montserrat",sans-serif;font-weight:700;text-transform:uppercase;line-height:1.1}
.brand .name{font-size:17px}
.brand .sub{font-size:8px;margin-top:3px}
.contact-bar{position:absolute;top:29px;color:var(--white);font-size:14px;display:flex;align-items:center;gap:8px}
.main-nav{position:absolute;top:74px;left:0;height:26px;width:1200px;font-family:"Montserrat",sans-serif;font-weight:500;font-size:12.5px;color:var(--white)}
.main-nav span{position:absolute;top:6px;display:flex;align-items:center;gap:6px}
.main-nav .active{top:0;height:26px;padding:0 8px;background:var(--navy);display:flex;align-items:center}

/* hero */
.hero-photo{left:0;top:121px;width:1200px;height:570px;background:linear-gradient(100deg,#cfc9bf 0%,#e7e2da 30%,#bfb8ad 55%,#8c7d6c 78%,#c06a45 100%)}
.hero-title{position:absolute;left:681px;top:248px;font-family:"Montserrat",sans-serif;font-weight:900;font-size:57px;line-height:68px;color:var(--white);text-transform:uppercase}
.slider-dots .dot{position:absolute;left:157px;width:24px;height:24px;border:1.5px solid var(--navy);border-radius:50%;font-size:11px;color:var(--navy);display:flex;align-items:center;justify-content:center;font-family:"Montserrat",sans-serif}
.slider-dots .dot.on{background:var(--navy);color:var(--white)}

/* welcome */
.welcome-kicker{left:150px;top:730px;font-size:18px}
.welcome-title{left:150px;top:762px;font-size:37px;line-height:44px;width:430px}
.body-text{position:absolute;font-size:13px;line-height:19.5px;color:var(--body)}

/* services */
.services-band{left:0;top:1211px;width:1200px;height:680px;background:var(--mist)}
.service-card{position:absolute;top:1380px;height:344px;width:288px}
.service-label{position:absolute;top:1743px;font-family:"Montserrat",sans-serif;font-weight:700;font-size:14px;color:var(--navy);text-transform:uppercase}
.service-label::after{content:"";position:absolute;left:0;top:28px;width:32px;height:1.5px;background:var(--line)}
.deco-frames{position:absolute;width:100px;height:100px}
.deco-frames i{position:absolute;border:1.5px solid var(--navy)}

/* audience boxes */
.audience{position:absolute;top:2383px;width:289px;height:92px;border:1.5px solid var(--navy);display:flex;align-items:center;padding-left:18px;gap:22px;background:var(--white)}
.audience .mark{width:52px;height:52px;border-radius:50%;background:var(--navy);flex:none;display:flex;align-items:center;justify-content:center}
.audience p{font-family:"Montserrat",sans-serif;font-weight:500;font-size:14px;line-height:19px;color:var(--navy)}
.chev{position:absolute;width:22px;height:34px}

/* mission */
.mission-band{left:0;top:2542px;width:1200px;height:334px;background:var(--mist)}
.value-card{position:absolute;top:2597px;width:433px;height:230px;background:var(--navy);color:var(--white);padding:38px 42px 0}
.value-card h3{font-family:"Montserrat",sans-serif;font-weight:800;font-size:38px;letter-spacing:.5px;margin-bottom:12px}
.value-card p{font-size:13.5px;line-height:22px;width:340px}

/* partners */
.partner{position:absolute;top:3066px;width:170px;height:84px;border:1.5px solid #c7cdd8;display:flex;align-items:center;justify-content:center}
.partner .badge{background:#3a3a3a}

/* cta */
.cta-photo{left:0;top:3229px;width:1200px;height:540px;background:linear-gradient(90deg,#3e4a3a 0%,#6a7460 28%,#c9cfc2 55%,#e8e6df 75%,#d4b58d 100%)}
.cta-title{position:absolute;left:158px;top:3300px;font-family:"Montserrat",sans-serif;font-weight:900;font-size:44px;line-height:50px;color:var(--white);text-transform:uppercase}
.cta-text{position:absolute;left:161px;top:3430px;width:380px;font-weight:300;font-size:23px;line-height:30px;color:var(--white)}

/* footer */
.site-footer{position:absolute;left:0;top:3760px;width:1200px;height:387px;background:var(--black);color:var(--white)}
.footer-brand{position:absolute;left:161px;top:160px;color:var(--navy);font-family:"Montserrat",sans-serif;font-weight:700;text-transform:uppercase;line-height:1.1}
.footer-brand .name{font-size:26px}
.footer-brand .sub{font-size:11px;margin-top:4px}
.footer-col{position:absolute;top:47px}
.footer-col h4{font-family:"Montserrat",sans-serif;font-weight:700;font-size:14.5px;margin-bottom:14px}
.footer-col li{list-style:none;font-size:12px;line-height:21px;color:#e8e8e8}
.footer-rule{position:absolute;left:153px;top:272px;width:895px;height:1px;background:#2e2e2e}
.follow{position:absolute;left:160px;top:316px;font-family:"Montserrat",sans-serif;font-weight:700;font-size:13px}
.social{position:absolute;top:312px;width:22px;height:22px;border-radius:50%;background:var(--white)}
.copyright{position:absolute;right:152px;top:318px;font-size:12px;color:#e0e0e0}
</style>
</head>
<body>

<header class="site-header">
  <div class="brand"><div class="name">Amber Crest</div><div class="sub">Health &amp; Wellness Group</div></div>
  <div class="contact-bar" style="left:553px">
    <svg width="16" height="12" viewBox="0 0 16 12" fill="none" stroke="#fff" stroke-width="1.2"><rect x=".6" y=".6" width="14.8" height="10.8"/><path d="M.6.6 8 7l7.4-6.4"/></svg>
    info@ambercresthealthandwellness.ca
  </div>
  <div class="contact-bar" style="left:896px">
    <svg width="16" height="16" viewBox="0 0 24 24" fill="none" stroke="#fff" stroke-width="1.6"><path d="M22 16.9v3a2 2 0 0 1-2.2 2 19.8 19.8 0 0 1-8.6-3.1 19.5 19.5 0 0 1-6-6A19.8 19.8 0 0 1 2.1 4.2 2 2 0 0 1 4.1 2h3a2 2 0 0 1 2 1.7c.1 1 .4 1.9.7 2.8a2 2 0 0 1-.5 2.1L8 9.9a16 16 0 0 0 6 6l1.3-1.3a2 2 0 0 1 2.1-.4c.9.3 1.8.6 2.8.7a2 2 0 0 1 1.8 2z"/></svg>
    +1 555 010 0199
  </div>
  <nav class="main-nav">
    <span class="active" style="left:370px">HOME</span>
    <span style="left:451px">ABOUT US <svg width="10" height="6" viewBox="0 0 10 6" fill="none" stroke="#fff"><path d="M1 1l4 4 4-4"/></svg></span>
    <span style="left:564px">SERVICES <svg width="10" height="6" viewBox="0 0 10 6" fill="none" stroke="#fff"><path d="M1 1l4 4 4-4"/></svg></span>
    <span style="left:670px">OUR TEAM <svg width="10" height="6" viewBox="0 0 10 6" fill="none" stroke="#fff"><path d="M1 1l4 4 4-4"/></svg></span>
    <span style="left:783px">JOIN OUR TEAM <svg width="10" height="6" viewBox="0 0 10 6" fill="none" stroke="#fff"><path d="M1 1l4 4 4-4"/></svg></span>
    <span style="left:926px">CONTACT</span>
    <span style="left:1020px">FAQ</span>
  </nav>
</header>

<section class="hero">
  <div class="photo hero-photo" role="img" aria-label="Smiling counsellor seated in an orange armchair holding a tablet in a bright office"></div>
  <div class="slider-dots">
    <span class="dot on" style="top:268px">1</span>
    <span class="dot" style="top:304px">2</span>
    <span class="dot" style="top:339px">3</span>
    <span class="dot" style="top:376px">4</span>
  </div>
  <h1 class="hero-title">Helping<br>those who<br>help others</h1>
  <a class="btn" style="left:688px;top:478px;width:214px;height:55px;font-size:19px">Join our team</a>
  <svg class="abs" style="left:0;top:640px" width="1200" height="60" viewBox="0 0 1200 60" preserveAspectRatio="none">
    <path d="M0 30 C300 8 520 10 760 22 S1080 40 1200 22 V60 H0Z" fill="#fff"/>
    <path d="M0 30 C300 8 520 10 760 22 S1080 40 1200 22" fill="none" stroke="#1f4580" stroke-width="7"/>
  </svg>
</section>

<section class="welcome">
  <p class="abs heading welcome-kicker">Welcome to</p>
  <h2 class="abs heading welcome-title">Amber Crest Health and Wellness Group</h2>
  <span class="rule" style="left:150px;top:915px"></span>
  <p class="body-text" style="left:150px;top:950px;width:410px">Sed ut perspiciatis unde omnis iste natus error sit voluptatem accusantium doloremque laudantium, totam rem aperiam, eaque ipsa quae ab illo inventore veritatis et quasi architecto beatae vitae dicta sunt explicabo. Nemo enim ipsam voluptatem quia voluptas sit aspernatur aut odit aut fugit, sed quia consequuntur magni dolores eos qui ratione voluptatem sequi nesciunt. Neque porro quisquam est, qui dolorem ipsum</p>
  <a class="btn" style="left:150px;top:1118px;width:129px;height:36px;font-size:12.5px">Read more</a>
  <div class="photo" style="left:625px;top:744px;width:409px;height:434px;border-radius:18px;background:linear-gradient(135deg,#e4e2de,#b8b4ab 50%,#3c4a3e)" role="img" aria-label="Two women talking on a green sofa during a counselling session"></div>
</section>

<section class="services">
  <div class="photo services-band"></div>
  <h2 class="abs heading" style="left:0;width:1200px;text-align:center;top:1266px;font-size:36px">Our services</h2>
  <span class="rule" style="left:576px;top:1332px"></span>
  <div class="deco-frames" style="left:117px;top:1347px"><i style="left:18px;top:0;width:76px;height:76px"></i><i style="left:9px;top:9px;width:76px;height:76px"></i><i style="left:0;top:18px;width:76px;height:76px"></i></div>
  <div class="service-card photo" style="left:150px;background:linear-gradient(160deg,#c7b59a,#9a7a55 55%,#6f5a45)" role="img" aria-label="Therapist listening to a client in a bright consulting room"></div>
  <div class="service-card photo" style="left:456px;background:linear-gradient(160deg,#2a0408,#b3121e 55%,#3a0507)" role="img" aria-label="Person resting under a red-light therapy panel"></div>
  <div class="abs" style="left:461px;top:1688px;width:278px;height:124px;background:#fff"></div>
  <p class="abs" style="left:482px;top:1707px;font-family:Montserrat,sans-serif;font-weight:700;font-size:14px;color:var(--navy)">RED-LIGHT THERAPY</p>
  <p class="abs" style="left:482px;top:1731px;width:240px;font-size:10.5px;line-height:14px">Sed ut perspiciatis unde omnis iste natus error sit voluptatem accusantium</p>
  <a class="btn" style="left:484px;top:1779px;width:97px;height:27px;font-size:10px">Read more</a>
  <div class="service-card photo" style="left:762px;background:linear-gradient(160deg,#e9d9c2,#c99b6a 60%,#9a6b44)" role="img" aria-label="Woman in a white robe relaxing in a warm salt therapy room with candles"></div>
  <div class="service-card photo" style="left:1068px;width:132px;background:linear-gradient(160deg,#8c8a7c,#5b5b54)" role="img" aria-label="Sound and vibration therapy with a singing bowl"></div>
  <p class="service-label" style="left:150px">Mental health &nbsp;therapy</p>
  <p class="service-label" style="left:762px">Salt therapy</p>
  <p class="service-label" style="left:1068px;white-space:nowrap">Sound &amp; vibration</p>
  <svg class="abs" style="left:1020px;top:1348px" width="64" height="64" viewBox="0 0 64 64">
    <circle cx="32" cy="32" r="30" fill="#1f4580" stroke="#fff" stroke-width="3"/>
    <path d="M27 24l-7 8 7 8M37 24l7 8-7 8" fill="none" stroke="#fff" stroke-width="2.2"/>
  </svg>
  <svg class="abs" style="left:0;top:1860px" width="1200" height="60" viewBox="0 0 1200 60" preserveAspectRatio="none">
    <path d="M0 22 C260 4 520 6 760 20 S1060 40 1200 26 V60 H0Z" fill="#fff"/>
    <path d="M0 22 C260 4 520 6 760 20 S1060 40 1200 26" fill="none" stroke="#1f4580" stroke-width="7"/>
  </svg>
</section>

<section class="who-we-serve">
  <div class="photo" style="left:150px;top:1978px;width:473px;height:358px;background:linear-gradient(120deg,#3f5a34,#8a6c46 40%,#d8b13c 60%,#6b4a35)" role="img" aria-label="Counsellor in a yellow cardigan speaking with a client"></div>
  <h2 class="abs heading" style="left:670px;top:1986px;font-size:36px">Who we serve</h2>
  <span class="rule" style="left:670px;top:2054px"></span>
  <p class="body-text" style="left:670px;top:2089px;width:385px;font-size:13.5px;line-height:22.5px">At Amber Crest Health &amp; Wellness Group, we specialize in providing compassionate, evidence-based care to individuals and organizations who face unique demands, elevated stress, and high-stakes environments. Our services are designed through a trauma-informed, culturally aware lens to ensure every client feels respected, understood, and supported.</p>
  <a class="btn" style="left:670px;top:2283px;width:130px;height:37px;font-size:12.5px">Read more</a>

  <svg class="chev" style="left:83px;top:2412px" viewBox="0 0 22 34" fill="none" stroke="#9aa3b3" stroke-width="2"><path d="M17 2 4 17l13 15"/></svg>
  <div class="audience" style="left:150px"><span class="mark"><svg width="24" height="24" viewBox="0 0 24 24" fill="none" stroke="#fff" stroke-width="2.4"><path d="M12 5v14M5 12h14"/></svg></span><p>First Responders &amp;<br>Frontline Professionals</p></div>
  <div class="audience" style="left:456px"><span class="mark"><svg width="24" height="24" viewBox="0 0 24 24" fill="none" stroke="#fff" stroke-width="2"><path d="M12 3l7 3v5c0 5-3 8-7 10-4-2-7-5-7-10V6z"/></svg></span><p>Public Safety &amp;<br>High-Stress<br>Occupations</p></div>
  <div class="audience" style="left:760px"><span class="mark"><svg width="26" height="24" viewBox="0 0 26 24" fill="none" stroke="#fff" stroke-width="2"><circle cx="8" cy="8" r="3.5"/><circle cx="18" cy="8" r="3.5"/><path d="M2 20c0-4 3-6 6-6s6 2 6 6M12 20c0-4 3-6 6-6s6 2 6 6"/></svg></span><p>Organizations &amp;<br>Community Partners</p></div>
  <svg class="chev" style="left:1088px;top:2412px" viewBox="0 0 22 34" fill="none" stroke="#9aa3b3" stroke-width="2"><path d="M5 2l13 15L5 32"/></svg>
</section>

<section class="mission-vision">
  <div class="photo mission-band"></div>
  <div class="deco-frames" style="left:117px;top:2560px"><i style="left:18px;top:0;width:76px;height:76px"></i><i style="left:9px;top:9px;width:76px;height:76px"></i><i style="left:0;top:18px;width:76px;height:76px"></i></div>
  <div class="deco-frames" style="left:988px;top:2762px"><i style="left:18px;top:0;width:76px;height:76px"></i><i style="left:9px;top:9px;width:76px;height:76px"></i><i style="left:0;top:18px;width:76px;height:76px"></i></div>
  <article class="value-card" style="left:150px">
    <h3>MISSION</h3>
    <p>To deliver compassionate, trauma-informed care that supports the mental, physical, and emotional well-being of first responders, frontline workers, and their families.</p>
    <svg class="abs" style="right:20px;top:22px" width="48" height="48" viewBox="0 0 48 48" fill="none" stroke="#fff" stroke-width="2.4"><circle cx="22" cy="26" r="17"/><circle cx="22" cy="26" r="10"/><circle cx="22" cy="26" r="3.5"/><path d="M22 26 40 8M34 8h6v6"/></svg>
  </article>
  <article class="value-card" style="left:617px">
    <h3>VISION</h3>
    <p>A community where those who serve have easy access to comprehensive, integrated wellness services that strengthen resilience, reduce stigma, and promote lifelong health.</p>
    <svg class="abs" style="right:18px;top:18px" width="54" height="50" viewBox="0 0 54 50" fill="none" stroke="#fff" stroke-width="2.4"><path d="M4 30c6-9 14-13 23-13s17 4 23 13c-6 9-14 13-23 13S10 39 4 30z"/><circle cx="27" cy="30" r="6" fill="#fff"/><path d="M27 2v6M13 6l3 5M41 6l-3 5"/></svg>
  </article>
</section>

<section class="partners">
  <h2 class="abs heading" style="left:0;width:1200px;text-align:center;top:2942px;font-size:36px">Community partners</h2>
  <span class="rule" style="left:576px;top:3013px"></span>
  <svg class="chev" style="left:83px;top:3091px" viewBox="0 0 22 34" fill="none" stroke="#9aa3b3" stroke-width="2"><path d="M17 2 4 17l13 15"/></svg>
  <div class="partner" style="left:150px"><span class="badge" style="width:90px;height:30px;border-radius:4px"></span></div>
  <div class="partner" style="left:332px"><span class="badge" style="width:96px;height:32px;border-radius:16px"></span></div>
  <div class="partner" style="left:516px"><span class="badge" style="width:100px;height:30px"></span></div>
  <div class="partner" style="left:699px"><span class="badge" style="width:82px;height:46px;border-radius:50%"></span></div>
  <div class="partner" style="left:883px"><span class="badge" style="width:58px;height:48px;border-radius:50%"></span></div>
  <svg class="chev" style="left:1088px;top:3091px" viewBox="0 0 22 34" fill="none" stroke="#9aa3b3" stroke-width="2"><path d="M5 2l13 15L5 32"/></svg>
</section>

<section class="cta">
  <div class="photo cta-photo" role="img" aria-label="Counsellor with a clipboard supporting a young woman seated on a beanbag by a bright window"></div>
  <h2 class="cta-title">Ready to take<br>the next step?</h2>
  <p class="cta-text">Supporting those who serve our community starts with accessible, compassionate care.</p>
  <a class="btn" style="left:164px;top:3533px;width:227px;height:43px;font-size:13px">Book a consultation</a>
  <a class="btn" style="left:164px;top:3594px;width:227px;height:43px;font-size:13px">Join our team</a>
</section>

<footer class="site-footer">
  <svg class="abs" style="left:0;top:-40px" width="1200" height="50" viewBox="0 0 1200 50" preserveAspectRatio="none">
    <path d="M0 18 C300 40 600 38 860 24 S1120 4 1200 10 V50 H0Z" fill="#000"/>
    <path d="M0 18 C300 40 600 38 860 24 S1120 4 1200 10" fill="none" stroke="#1f4580" stroke-width="7"/>
  </svg>
  <div class="footer-brand"><div class="name">Amber Crest</div><div class="sub">Health &amp; Wellness Group</div></div>
  <div class="footer-col" style="left:423px"><h4>ABOUT US</h4><ul><li>Our Story</li><li>Mission &amp; Vision</li><li>Who We Serve</li><li>Facility overview</li><li>Partner network</li></ul></div>
  <div class="footer-col" style="left:636px"><h4>SERVICES</h4><ul><li>Mental Health Therapy</li><li>Trauma &amp; First Responder support</li><li>Salt Therapy</li><li>Sound &amp; Vibration Therapy</li><li>Red-Light Therapy</li><li>PEMF Therapy</li><li>Neurofeedback</li><li>OT &amp; Rehabilitation</li></ul></div>
  <div class="footer-col" style="left:921px"><h4>JOIN OUR TEAM</h4><ul><li>Why join</li><li>Positions available</li><li>Requirements</li><li>Application process</li></ul></div>
  <div class="footer-rule"></div>
  <p class="follow">FOLLOW US</p>
  <span class="social" style="left:266px"></span>
  <span class="social" style="left:295px"></span>
  <span class="social" style="left:324px"></span>
  <span class="social" style="left:353px"></span>
  <span class="social" style="left:382px"></span>
  <p class="copyright">Copyright © 2025 All Rights Reserved</p>
</footer>

</body>
</html>
```